Butcher shop

We have 2 butcher shops:

Shop 9, Ridgeway Court, Aberdeen NSW 2336
Ph 02 6512 3840

47 Marlow St, Scone NSW 2337
Ph 02 6518 2274

ABN 48 907 215 816

I would like this info on reverse of card and my personal info on front of card. I have a logo I would like to use also. Require a very smooth thick matte card, with colour both sides.

Front of card should say:

Linda Farrugia
Accounts

Ph 0437 620 915
E lindafarrugia@quollmail.com.au

Industry/Entity Type

Shop

Contact Information for Business Card

Linda Farrugia
Ph 0437 620 915

Logo Text

Farrugia's Quality Meats

Logo styles of interest
Pictorial/Combination Logo
Requirements
Must have
• We use Century Gothic Font

```html
<!DOCTYPE html>
<html lang="en">
<head>
<meta charset="utf-8">
<title>Farrugia's Quality Meats – Business Card</title>
<link href="https://fonts.googleapis.com/css2?family=Didact+Gothic&display=swap" rel="stylesheet">
<style>
  :root {
    --backdrop: #2a2a2a;
    --sky-light: #a9e0f6;
    --sky: #8dd1ee;
    --sky-deep: #6fb8d6;
    --band: #e4e6e8;
    --band-edge: #f4f5f6;
    --ink: #14212b;
    --ink-soft: #2c3a44;
  }
  * { margin: 0; padding: 0; box-sizing: border-box; }
  html, body {
    width: 1200px; height: 901px; overflow: hidden;
    background: var(--backdrop);
    font-family: "Didact Gothic", "Century Gothic", sans-serif;
    color: var(--ink);
  }
  .stage {
    position: relative; width: 1200px; height: 901px;
    display: flex; justify-content: center; align-items: center; gap: 80px;
  }
  .card {
    position: relative; width: 330px; height: 540px;
    border-radius: 26px; overflow: hidden;
    background: linear-gradient(180deg, var(--sky-light) 0%, var(--sky) 100%);
    box-shadow: 0 14px 30px rgba(0,0,0,0.45);
  }
  .brand {
    position: absolute; left: 0; right: 0;
    display: flex; flex-direction: column; align-items: center;
  }
  .brand-mark {
    width: 26px; height: 26px; border-radius: 50%;
    background: var(--ink); margin-bottom: 18px;
  }
  .brand-name {
    font-size: 31px; line-height: 1.08; text-align: center; color: var(--ink);
    letter-spacing: 0.2px;
  }
  /* reverse side */
  .card-reverse .brand { top: 118px; }
  .locations {
    position: absolute; right: 30px; top: 330px;
    text-align: right; font-size: 14px; line-height: 1.45; color: var(--ink-soft);
  }
  .location + .location { margin-top: 22px; }
  .abn { margin-top: 14px; font-size: 9px; letter-spacing: 0.3px; }
  /* front side */
  .card-front .brand { top: 56px; }
  .card-front .brand-name { font-size: 29px; }
  .person-band {
    position: absolute; left: 0; right: 0; top: 252px; height: 210px;
    background: linear-gradient(180deg, var(--band-edge) 0%, var(--band) 100%);
    text-align: center; padding-top: 54px;
  }
  .person-name { font-size: 20px; color: var(--ink); }
  .person-role { font-size: 12px; color: var(--ink-soft); margin-top: 2px; }
  .person-contact { margin-top: 22px; font-size: 13px; line-height: 1.55; color: var(--ink-soft); }
  .footer-strip {
    position: absolute; left: 0; right: 0; bottom: 0; height: 78px;
    background: linear-gradient(180deg, var(--sky-deep) 0%, #7cc3e0 100%);
  }
  .footer-strip::before {
    content: ""; position: absolute; left: 0; right: 0; top: 0; height: 14px;
    background: #86c8e3;
  }
</style>
</head>
<body>
<main class="stage">
  <section class="card card-reverse" aria-label="Card reverse">
    <div class="brand">
      <span class="brand-mark"></span>
      <p class="brand-name">Farrugia's<br>Quality Meats</p>
    </div>
    <div class="locations">
      <div class="location">
        <p>Shop 9, Ridgeway Court</p>
        <p>Aberdeen NSW 2336</p>
        <p>p: 02 6512 3840</p>
      </div>
      <div class="location">
        <p>47 Marlow St, Scone NSW 2337</p>
        <p>p: 02 6518 2274</p>
      </div>
      <p class="abn">ABN 48 907 215 816</p>
    </div>
  </section>

  <section class="card card-front" aria-label="Card front">
    <div class="brand">
      <span class="brand-mark"></span>
      <p class="brand-name">Farrugia's<br>Quality Meats</p>
    </div>
    <div class="person-band">
      <p class="person-name">Linda Farrugia</p>
      <p class="person-role">Accounts</p>
      <div class="person-contact">
        <p>e: lindafarrugia@quollmail.com.au</p>
        <p>p: 0437 620 915</p>
      </div>
    </div>
    <div class="footer-strip"></div>
  </section>
</main>
</body>
</html>
```